Brochure Design Project

This will be a tri-fold full 8.5x11 brochure that will be distributed and sitting in Oncology offices all throughout the US. It is a lead generation and referral designed piece that it to target all patients, Cancer primarily, but all critically ill patients and seniors above the age of 70. We want our service to go beyond just a financial transaction, we want to educate patients of their rights within a life insurance policy and if we cannot help them personally, do want to assist them by referring them to other agencies and non profits than can. ( I want to redesign the brochure attached, it can be very similar and need only minor changes to content, but would welcome all suggestions on improving message, and in gaining attention, picture substitutions and change of colors, along with the layout itself can be improved upon, and I need this piece to look very professional and appropriate for medical offices. I will be needing assistance on several upcoming projects and will also have great printing demands.

Target Market(s)

Cancer patients
all chronically and critically ill patients
all seniors above age 70

Industry/Entity Type

Life Insurance

Requirements
Must have
• Cancer and the terminally ill
Nice to have
• seniors above 70

```html
<!DOCTYPE html>
<html lang="en">
<head>
<meta charset="utf-8">
<title>Beacon Settlements Tri-fold Brochure</title>
<link href="https://fonts.googleapis.com/css2?family=Open+Sans:wght@400;600;700;800&display=swap" rel="stylesheet">
<style>
  :root {
    --page-bg: #f2f0ec;
    --panel-grey: #e4e4e6;
    --panel-light: #ececee;
    --card-white: #fbfbfb;
    --brand-blue: #4677be;
    --ink: #222226;
    --ink-soft: #3a3a3e;
    --gold-1: #8a6a2c;
    --gold-2: #f0c256;
    --divider: #c9c9cc;
  }
  * { box-sizing: border-box; margin: 0; padding: 0; }
  html, body { width: 1200px; height: 960px; overflow: hidden; }
  body {
    background: var(--page-bg);
    font-family: "Open Sans", Arial, sans-serif;
    color: var(--ink);
  }
  .brochure {
    position: absolute; left: 30px; top: 40px;
    width: 1140px; height: 880px;
    display: flex;
    box-shadow: 0 2px 10px rgba(0,0,0,.18);
  }
  .panel {
    position: relative; width: 380px; height: 880px;
    border-right: 1px solid var(--divider);
    overflow: hidden;
  }
  .panel:last-child { border-right: none; }

  .gold-rule {
    position: absolute; left: 0; right: 0; height: 5px;
    background: linear-gradient(90deg, var(--gold-1), var(--gold-2) 55%, var(--gold-1));
    box-shadow: 0 2px 3px rgba(0,0,0,.25);
  }

  .brand {
    display: flex; align-items: center; justify-content: center; gap: 10px;
    color: var(--brand-blue); font-weight: 700;
  }
  .brand-dot { border-radius: 50%; background: var(--brand-blue); flex: none; }
  .brand-name { letter-spacing: 1px; line-height: 1.1; text-align: center; }

  /* Panel 1: reply panel */
  .reply-top {
    position: absolute; left: 0; top: 0; width: 100%; height: 261px;
    background: var(--panel-grey); text-align: center;
  }
  .reply-top .brand { position: absolute; top: 42px; left: 0; right: 0; }
  .reply-top .brand-dot { width: 16px; height: 16px; }
  .reply-top .brand-name { font-size: 26px; }
  .reply-prompt {
    position: absolute; top: 112px; left: 0; right: 0;
    font-size: 16px; line-height: 22px; color: var(--ink-soft);
  }
  .reply-phone {
    position: absolute; top: 158px; left: 0; right: 0;
    font-size: 40px; font-weight: 700; color: #333;
  }
  .reply-note {
    position: absolute; top: 208px; left: 0; right: 0;
    font-size: 15px; line-height: 21px; color: var(--ink-soft);
  }
  .postcard {
    position: absolute; left: 0; top: 266px; width: 100%; height: 614px;
    background: var(--card-white);
  }
  .postcard-face {
    position: absolute; left: 380px; top: 0;
    width: 611px; height: 380px;
    transform-origin: top left; transform: rotate(90deg);
  }
  .brm-box {
    position: absolute; left: 66px; top: 150px; width: 346px; height: 62px;
    border: 2px solid #333; padding: 2px 8px;
  }
  .brm-title { font-size: 27px; font-weight: 800; line-height: 32px; letter-spacing: .5px; }
  .brm-permit { display: flex; justify-content: space-between; font-size: 14px; line-height: 20px; }
  .postage-note { position: absolute; left: 137px; top: 213px; font-size: 11px; letter-spacing: .3px; }
  .addressee { position: absolute; left: 137px; top: 240px; font-size: 21px; font-weight: 700; }
  .address-line { position: absolute; left: 66px; top: 272px; font-size: 18px; }
  .address-city { position: absolute; left: 192px; top: 302px; font-size: 18px; }
  .no-postage {
    position: absolute; left: 452px; top: 46px; width: 137px; height: 107px;
    border: 1px solid #555; color: var(--brand-blue);
    font-size: 13px; line-height: 18px; text-align: center; padding-top: 8px;
  }

  /* Panel 2: benefits */
  .photo {
    position: absolute; left: 0; width: 100%;
  }
  .photo-care {
    top: 0; height: 259px;
    background: linear-gradient(120deg, #d9d2c6 0%, #c9b9a4 40%, #b8473a 62%, #e0713a 80%, #e7e1d8 100%);
  }
  .benefits {
    position: absolute; left: 0; top: 266px; width: 100%; height: 614px;
    background: var(--panel-light);
  }
  .benefits-title {
    position: absolute; left: 45px; top: 36px;
    font-size: 23px; font-weight: 700; color: var(--brand-blue);
  }
  .benefit-list {
    position: absolute; left: 26px; top: 68px; right: 20px;
    list-style: none; font-size: 17px; line-height: 24.2px; color: var(--ink-soft);
  }
  .benefit-list li { position: relative; padding-left: 14px; }
  .benefit-list li::before {
    content: ""; position: absolute; left: 0; top: 10px;
    width: 5px; height: 5px; border-radius: 50%; background: var(--brand-blue);
  }
  .benefits-sign {
    position: absolute; left: 41px; top: 532px;
    font-size: 26px; line-height: 35px; font-weight: 700; color: var(--brand-blue);
  }

  /* Panel 3: cover */
  .cover-top {
    position: absolute; left: 0; top: 0; width: 100%; height: 348px;
    background: var(--panel-grey);
  }
  .cover-top .brand { position: absolute; top: 62px; left: 0; right: 0; }
  .cover-top .brand-dot { width: 20px; height: 20px; }
  .cover-top .brand-name { font-size: 32px; }
  .cover-headline {
    position: absolute; left: 30px; top: 143px;
    font-size: 64px; line-height: 64px; font-weight: 700; color: var(--brand-blue);
    letter-spacing: -.5px;
  }
  .photo-seniors {
    top: 348px; height: 257px;
    background: linear-gradient(110deg, #e9e3da 0%, #dfc3ad 30%, #d8b79c 55%, #efe8df 100%);
  }
  .cover-bottom {
    position: absolute; left: 0; top: 612px; width: 100%; height: 268px;
    background: var(--panel-light);
  }
  .cover-reassure {
    position: absolute; left: 36px; top: 30px;
    font-size: 27px; line-height: 38px; font-weight: 700; color: var(--ink);
  }
  .cover-phone {
    position: absolute; left: 34px; top: 163px;
    font-size: 49px; font-weight: 700; color: var(--ink);
  }
  .cover-tagline {
    position: absolute; left: 30px; top: 223px;
    font-size: 25px; color: var(--brand-blue);
  }
</style>
</head>
<body>
<main class="brochure">

  <section class="panel panel-reply">
    <div class="reply-top">
      <div class="brand"><span class="brand-dot"></span><span class="brand-name">Beacon Settlements</span></div>
      <p class="reply-prompt">Please return the attached postcard or<br>Call Toll Free</p>
      <p class="reply-phone">800-555-0147</p>
      <p class="reply-note">All Communication will<br>be kept strictly confidential!</p>
    </div>
    <div class="gold-rule" style="top:261px"></div>
    <div class="postcard">
      <div class="postcard-face">
        <div class="brm-box">
          <p class="brm-title">BUSINESS REPLY MAIL</p>
          <p class="brm-permit"><span>First-Class Mail</span><span>Permit No. 2207</span><span>GEORGIA</span></p>
        </div>
        <p class="postage-note">POSTAGE WILL BE PAID BY ADDRESSEE</p>
        <p class="addressee">BEACON SETTLEMENTS</p>
        <p class="address-line">480 Willow Creek Dr. Marietta,</p>
        <p class="address-city">Georgia 30060</p>
        <div class="no-postage">NO POSTAGE<br>NECESSARY<br>IF MAILED<br>IN THE<br>UNITED STATES</div>
      </div>
    </div>
  </section>

  <section class="panel panel-benefits">
    <div class="photo photo-care" role="img" aria-label="Photo of a smiling caregiver in an orange apron comforting a patient in a hospital ward"></div>
    <div class="gold-rule" style="top:259px"></div>
    <div class="benefits">
      <h2 class="benefits-title">BEACON SETTLEMENTS</h2>
      <ul class="benefit-list">
        <li>Reduce  financial Stress</li>
        <li>Pay for Uninsured Healthcare Cost</li>
        <li>Pay for Alternative Treatment</li>
        <li>Improve Quality of Life</li>
        <li>pay off Debt</li>
        <li>Take a Long Awaited vacation or Dream Trip</li>
        <li>Make Cash Gifts to family and Friends</li>
        <li>Fulfill Life Wishes</li>
        <li>Pay for College Funding</li>
        <li>Make Home Improvements</li>
        <li>Donate to Church or Charity</li>
        <li>See the Money Enjoyed by Relatives Now</li>
        <li>Invest in Financial Vehicles</li>
        <li>Buy a New car</li>
        <li>Fund Long Term Care Expenses</li>
        <li>Plan Ahend for Final Estate Needs</li>
      </ul>
      <p class="benefits-sign">HOPE IS OUR DESIRED<br>GIFT TO YOU!</p>
    </div>
  </section>

  <section class="panel panel-cover">
    <div class="cover-top">
      <div class="brand"><span class="brand-dot"></span><span class="brand-name">Beacon Settlements</span></div>
      <h1 class="cover-headline">DISCOVER<br>FINANCIAL<br>FREEDOM</h1>
    </div>
    <div class="photo photo-seniors" role="img" aria-label="Photo of four cheerful seniors giving thumbs up"></div>
    <div class="gold-rule" style="top:605px"></div>
    <div class="cover-bottom">
      <p class="cover-reassure">YOU ARE NOT ALONE<br>FINANCIAL RESOURCES<br>ARE AVAILABLE!</p>
      <p class="cover-phone">800-555-0147</p>
      <p class="cover-tagline">WE ARE WAITING TO HELP!</p>
    </div>
  </section>

</main>
</body>
</html>
```